Electrician Company Website Design

I am looking to get a website designed only. I do not need it converted ot html. I simply need the design in a psd format. I have my own team for the conversion. The website is for an electrician company called Bramblecourt electric. I have created a txt document with the project parameters and specifics. I have also uploaded their logo in all avaible formats. It's a zip file.

Number of Pages Required

1 page

```html
<!DOCTYPE html>
<html lang="en">
<head>
<meta charset="utf-8">
<title>Bramblecourt Electric</title>
<link href="https://fonts.googleapis.com/css2?family=Oswald:wght@500;600;700&family=Roboto:wght@400;500;700&display=swap" rel="stylesheet">
<style>
:root{
  --blue:#1f66b3;
  --blue-dark:#17579c;
  --red:#a3201f;
  --ink:#222;
  --text:#555;
  --line:#d9dde3;
  --white:#fff;
}
*{box-sizing:border-box;margin:0;padding:0}
html,body{width:1200px;height:3871px;overflow:hidden;background:var(--white)}
body{position:relative;font-family:Roboto,Arial,sans-serif;color:var(--text)}
.abs{position:absolute}
.head{font-family:Oswald,"Arial Narrow",sans-serif;font-weight:700;text-transform:uppercase;letter-spacing:.5px}
.btn{position:absolute;display:flex;align-items:center;justify-content:center;background:var(--red);color:#fff;font:700 14px Roboto,sans-serif;border-radius:30px;text-transform:uppercase}
.circle{position:absolute;border-radius:50%}
/* header */
.brand{left:110px;top:30px;display:flex;align-items:center;gap:12px}
.brand-mark{width:42px;height:42px;border-radius:50%;background:var(--red)}
.brand-name{font-family:Oswald,sans-serif;font-weight:700;font-size:24px;color:var(--blue);text-transform:uppercase;line-height:1.05;width:160px}
.info-label{font-size:14px;color:#666}
.info-value{font-size:16px;font-weight:700;color:var(--ink);line-height:21px;margin-top:4px}
.social{width:34px;height:34px;border-radius:50%}
/* nav */
.nav{left:0;top:146px;width:903px;height:59px;background:var(--blue);border-radius:0 30px 30px 0}
.nav a{position:absolute;top:0;height:59px;line-height:59px;color:#fff;font:700 14px Roboto,sans-serif;text-decoration:none;text-transform:uppercase}
.nav .active{background:var(--red);left:87px;width:86px;text-align:center}
/* hero */
.hero{left:0;top:205px;width:1200px;height:653px;background:linear-gradient(110deg,#e8ebee 0%,#c9d0d6 35%,#8a8f94 60%,#4c5560 85%,#2d3440 100%)}
/* services */
.svc-intro{left:111px;top:781px;width:232px;height:332px;background:var(--blue);border-radius:0 32px 32px 0;padding:30px 27px;color:#fff}
.svc-card{top:781px;width:233px;height:154px;border:1px solid var(--line);border-bottom:none;background:#fff;border-radius:34px 34px 0 0;padding:27px 30px}
.svc-card h3{font-family:Oswald,sans-serif;font-weight:600;font-size:17px;color:var(--blue);line-height:25px;text-transform:uppercase}
.svc-num{position:absolute;right:30px;top:82px;font-family:Oswald,sans-serif;font-size:46px;color:transparent;-webkit-text-stroke:1px #a9c3e2}
.plus{position:absolute;width:30px;height:30px;border-radius:50%;background:var(--blue);color:#fff;font-size:16px;line-height:30px;text-align:center}
.svc-text{position:absolute;font-size:14px;line-height:26px;color:var(--text);width:180px;text-align:justify}
p.body{font-size:14px;line-height:26px;text-align:justify}
</style>
</head>
<body>

<!-- Header -->
<div class="abs brand"><span class="brand-mark"></span><span class="brand-name">Bramblecourt Electric</span></div>

<svg class="abs" style="left:452px;top:45px" width="40" height="54" viewBox="0 0 40 54"><path d="M20 2C10 2 2 10 2 20c0 13 18 31 18 31s18-18 18-31C38 10 30 2 20 2z" fill="none" stroke="#a3201f" stroke-width="2"/><circle cx="20" cy="20" r="7" fill="none" stroke="#a3201f" stroke-width="2"/></svg>
<div class="abs" style="left:507px;top:42px"><div class="info-label">OFFICE ADDRESS :</div><div class="info-value">1427 LARKFIELD AVE NE<br>MILBROOK, MN 55099</div></div>

<svg class="abs" style="left:725px;top:46px" width="40" height="46" viewBox="0 0 40 46"><path d="M8 3l8 10-5 5c3 7 8 12 15 15l5-5 9 8-6 8C20 42 3 25 2 9z" fill="none" stroke="#a3201f" stroke-width="2" stroke-linejoin="round"/></svg>
<div class="abs" style="left:773px;top:42px"><div class="info-label">PHONE :</div><div class="info-value">555 014 2286</div></div>

<div class="abs social" style="left:966px;top:52px;background:#3b5aa0"></div>
<div class="abs social" style="left:1010px;top:52px;background:#2aa0e6"></div>
<div class="abs social" style="left:1053px;top:52px;background:#d93a30"></div>

<!-- Navigation -->
<nav class="abs nav">
  <a class="active">Home</a>
  <a style="left:224px">Service Area</a>
  <a style="left:395px">Services</a>
  <a style="left:535px">Contact</a>
  <a style="left:673px">Gallery</a>
  <a style="left:808px">FAQs</a>
</nav>
<div class="btn" style="left:920px;top:146px;width:257px;height:59px;border-radius:30px 30px 30px 30px">Get a Quote</div>

<!-- Hero -->
<div class="abs hero" role="img" aria-label="Smiling electrician in a hard hat holding a tablet on a rooftop with solar panels above a city"></div>
<div class="abs head" style="left:110px;top:352px;font-size:21px;color:var(--red);font-weight:600">Welcome to</div>
<div class="abs head" style="left:108px;top:382px;font-size:74px;line-height:76px;color:var(--ink)">Bramblecourt<br>Electric</div>
<div class="btn" style="left:110px;top:556px;width:201px;height:60px">Get Started</div>
<svg class="abs" style="left:1130px;top:465px" width="70" height="100"><circle cx="13" cy="13" r="10" fill="none" stroke="#a3201f" stroke-width="2"/><circle cx="13" cy="13" r="5" fill="#a3201f"/><line x1="23" y1="13" x2="70" y2="13" stroke="#a3201f" stroke-width="2"/><circle cx="13" cy="38" r="6" fill="#fff"/><circle cx="13" cy="63" r="6" fill="#fff"/><circle cx="13" cy="88" r="6" fill="#fff"/></svg>

<!-- Services -->
<div class="abs svc-intro">
  <div class="head" style="font-size:44px;line-height:60px;font-weight:600">Our<br>Services</div>
  <p class="body" style="margin-top:18px;font-size:14px;line-height:26px;color:#fff">Lorem ipsum dolor sit am et, consectetur adipis cing elit, sed do eiusmod temp or incididunt ut labore et dolore magna aliqua.</p>
</div>

<div class="abs svc-card" style="left:360px"><h3>Commerical<br>Electrical Services</h3><div class="svc-num">01</div>
<svg class="abs" style="left:30px;top:82px" width="42" height="42" viewBox="0 0 42 42" fill="none" stroke="#a3201f" stroke-width="2"><path d="M4 38L30 12M10 4l28 28M34 4l4 4-6 6-4-4zM4 32l6 6"/></svg></div>
<div class="abs svc-card" style="left:607px"><h3>Residential<br>Electrical Services</h3><div class="svc-num">02</div>
<svg class="abs" style="left:30px;top:82px" width="42" height="42" viewBox="0 0 42 42" fill="none" stroke="#a3201f" stroke-width="2"><path d="M10 16a11 11 0 0 1 22 0zM14 16v4a7 7 0 0 0 14 0v-4M8 40c0-8 6-12 13-12s13 4 13 12"/></svg></div>
<div class="abs svc-card" style="left:855px"><h3>Industrial<br>Electrical Services</h3><div class="svc-num">03</div>
<svg class="abs" style="left:30px;top:82px" width="42" height="42" viewBox="0 0 42 42" fill="none" stroke="#a3201f" stroke-width="2"><rect x="10" y="6" width="22" height="26" rx="3"/><path d="M16 6v26M22 6v26M28 6v26M4 18h6M32 18h6"/><circle cx="10" cy="36" r="4"/></svg></div>

<div class="plus" style="left:392px;top:918px">+</div>
<div class="plus" style="left:639px;top:918px">+</div>
<div class="plus" style="left:887px;top:918px">+</div>

<div class="svc-text" style="left:390px;top:965px">Lorem ipsum dolor sit am et, consectetur adipis cing elit, sed do eiusmod temp or incididunt ut labore et dolore magna aliqua.</div>
<div class="svc-text" style="left:637px;top:965px">Lorem ipsum dolor sit am et, consectetur adipis cing elit, sed do eiusmod temp or incididunt ut labore et dolore magna aliqua.</div>
<div class="svc-text" style="left:885px;top:965px">Lorem ipsum dolor sit am et, consectetur adipis cing elit, sed do eiusmod temp or incididunt ut labore et dolore magna aliqua.</div>

<!-- About -->
<div class="abs" style="left:93px;top:1500px;width:190px;height:187px;background:var(--red);border-radius:60px 0 0 0"></div>
<div class="abs" role="img" aria-label="Smiling electrician in hard hat and safety vest wiring an electrical panel" style="left:111px;top:1216px;width:471px;height:454px;border-radius:30px 40px 40px 0;background:linear-gradient(90deg,#7c8790 0%,#b8c0c6 45%,#d7d9d2 70%,#eceeea 100%)"></div>
<div class="abs" style="left:617px;top:1214px;font-size:14px;letter-spacing:5px;color:var(--red)">ABOUT US</div>
<div class="abs head" style="left:614px;top:1232px;font-size:51px;color:var(--blue);font-weight:600">Bramblecourt Electric</div>
<p class="abs body" style="left:617px;top:1306px;width:472px">Lorem ipsum dolor sit amet, consectetur adipiscing elit, sed do eiusmod tempor incididunt ut labore et dolore magna aliqua. Ut enim ad minim veniam, quis nostrud exercitation ullamco laboris nisi ut aliquip ex ea commodo consequat. Duis aute irure dolor in reprehenderit in voluptate velit esse cillum dolore eu fugiat nulla pariatur.</p>
<p class="abs body" style="left:617px;top:1460px;width:472px">Excepteur sint occaecat cupidatat non proident, sunt in culpa qui officia deserunt mollit anim id est laborum. Lorem ipsum dolor sit amet, consectetur adipiscing elit, sed do eiusmod tempor incididunt ut labore et dolore magna aliqua. Ut enim ad minim veniam, quis nostrud exercitation ullamco laboris nisi ut aliquip ex ea commodo consequat.</p>
<div class="btn" style="left:617px;top:1610px;width:201px;height:58px">Learn More ›</div>

<!-- Service area -->
<div class="abs" style="left:0;top:1772px;width:1200px;height:634px;background:linear-gradient(135deg,var(--blue) 0%,#2a72bd 50%,var(--blue-dark) 100%)"></div>
<div class="abs head" style="left:111px;top:1890px;font-size:50px;color:#fff;font-weight:600">Services Area</div>
<p class="abs body" style="left:111px;top:1973px;width:473px;color:#fff">Lorem ipsum dolor sit amet, consectetur adipiscing elit, sed do eiusmod tempor incididunt ut labore et dolore magna aliqua. Ut enim ad minim veniam, quis nostrud exercitation ullamco laboris nisi ut aliquip ex ea commodo consequat. Duis aute irure dolor in reprehenderit in voluptate velit esse cillum dolore eu fugiat nulla pariatur.</p>
<svg class="abs" style="left:0;top:0;overflow:visible" width="1" height="1">
  <defs><path id="pin" d="M6 0a6 6 0 0 0-6 6c0 5 6 11 6 11s6-6 6-11a6 6 0 0 0-6-6z" fill="#a3201f"/></defs>
  <use href="#pin" x="110" y="2129"/><use href="#pin" x="281" y="2129"/><use href="#pin" x="453" y="2129"/>
  <use href="#pin" x="110" y="2181"/><use href="#pin" x="281" y="2181"/>
</svg>
<div class="abs" style="left:137px;top:2127px;font:700 18px Roboto,sans-serif;color:#fff">Chisago MN</div>
<div class="abs" style="left:308px;top:2127px;font:700 18px Roboto,sans-serif;color:#fff">Pine MN</div>
<div class="abs" style="left:480px;top:2127px;font:700 18px Roboto,sans-serif;color:#fff">Isanti MN</div>
<div class="abs" style="left:137px;top:2179px;font:700 18px Roboto,sans-serif;color:#fff">Anoka MN</div>
<div class="abs" style="left:308px;top:2179px;font:700 18px Roboto,sans-serif;color:#fff">Washington MN</div>
<div class="btn" style="left:112px;top:2236px;width:201px;height:59px">Learn More ›</div>
<div class="abs" role="img" aria-label="Outline map of Minnesota counties with location pins" style="left:684px;top:1872px;width:360px;height:416px;background:rgba(255,255,255,.12);border-radius:8px"></div>

<!-- Gallery -->
<div class="abs head" style="left:0;top:2497px;width:1200px;text-align:center;font-size:50px;color:var(--blue);font-weight:600">Project Gallery</div>
<div class="abs" role="img" aria-label="Electrician in blue cap working on a wall fixture from a ladder" style="left:110px;top:2591px;width:315px;height:315px;background:linear-gradient(135deg,#dfe2e4,#5a7ea8)"></div>
<div class="abs" role="img" aria-label="Smiling electrician in cap working on a panel" style="left:441px;top:2591px;width:316px;height:315px;background:linear-gradient(135deg,#c9cdd2,#3e5a80)"></div>
<div class="circle" style="left:569px;top:2717px;width:62px;height:62px;background:#fff;color:var(--blue);font-size:34px;text-align:center;line-height:60px">+</div>
<div class="abs" role="img" aria-label="Engineer in red hard hat holding a clipboard" style="left:773px;top:2591px;width:315px;height:315px;background:linear-gradient(135deg,#6f7378,#2b3442)"></div>
<div class="abs" role="img" aria-label="Technician connecting network cables in a server rack" style="left:110px;top:2921px;width:315px;height:315px;background:linear-gradient(135deg,#4a6aa0,#c8c9cc)"></div>
<div class="abs" role="img" aria-label="Electrician in orange hard hat working on a breaker panel" style="left:441px;top:2921px;width:316px;height:315px;background:linear-gradient(135deg,#b5b8bb,#e8e6e2)"></div>
<div class="abs" role="img" aria-label="Worker in yellow hard hat and vest with a laptop" style="left:773px;top:2921px;width:315px;height:315px;background:linear-gradient(135deg,#8a8c90,#c7d25a)"></div>

<!-- Footer -->
<div class="abs" style="left:0;top:3388px;width:1200px;height:483px;background:var(--blue)"></div>
<div class="abs head" style="left:110px;top:3483px;font-size:21px;color:#fff;font-family:Roboto,sans-serif">Quick Links</div>
<div class="abs" style="left:110px;top:3532px;font-size:14px;line-height:26px;color:#fff">
  <div>»&nbsp;&nbsp;&nbsp;Company</div><div>»&nbsp;&nbsp;&nbsp;Service Area</div><div>»&nbsp;&nbsp;&nbsp;Services</div><div>»&nbsp;&nbsp;&nbsp;Contact</div><div>»&nbsp;&nbsp;&nbsp;Gallery</div><div>»&nbsp;&nbsp;&nbsp;FAQs</div>
</div>
<div class="abs head" style="left:350px;top:3483px;font-size:21px;color:#fff;font-family:Roboto,sans-serif">Contact Us</div>
<div class="abs" style="left:350px;top:3532px;font-size:14px;line-height:26px;color:#fff">
  <div>●&nbsp;&nbsp;&nbsp;&nbsp;&nbsp;1427 Larkfield Ave NE</div>
  <div style="padding-left:34px">Milbrook, MN 55099</div>
  <div style="margin-top:24px">✆&nbsp;&nbsp;&nbsp;&nbsp;&nbsp;555 014 2286</div>
  <div style="margin-top:24px">✉&nbsp;&nbsp;&nbsp;&nbsp;&nbsp;hello@bramblecourt.example</div>
</div>
<div class="abs" style="left:110px;top:3738px;font-size:14px;color:#fff">Copyright © 2022 Company name | Privacy Policy | Terms &amp; Conditions</div>
<div class="circle" style="left:111px;top:3782px;width:36px;height:36px;border:2px solid #fff"></div>
<div class="circle" style="left:155px;top:3782px;width:36px;height:36px;border:2px solid #fff"></div>
<div class="circle" style="left:198px;top:3782px;width:36px;height:36px;border:2px solid #fff"></div>

<!-- Quote form -->
<div class="abs" style="left:614px;top:3336px;width:473px;height:487px;background:#fff;border-radius:34px;box-shadow:0 6px 20px rgba(0,0,0,.12)"></div>
<div class="abs head" style="left:614px;top:3362px;width:473px;text-align:center;font-size:48px;color:var(--blue);font-weight:600">Get a Free Quote</div>
<div class="abs" style="left:641px;top:3437px;width:200px;height:51px;border:1px solid var(--line);padding:17px;font-size:14px;color:#777">Name</div>
<div class="abs" style="left:856px;top:3437px;width:201px;height:51px;border:1px solid var(--line);padding:17px;font-size:14px;color:#777">Phone</div>
<div class="abs" style="left:641px;top:3504px;width:417px;height:51px;border:1px solid var(--line);padding:17px;font-size:14px;color:#777">Email address</div>
<div class="abs" style="left:641px;top:3572px;width:417px;height:140px;border:1px solid var(--line);padding:17px;font-size:14px;color:#777">Message</div>
<div class="btn" style="left:641px;top:3734px;width:199px;height:50px;border-radius:0">Submit Now</div>

</body>
</html>
```